Bottle & Jar Designs for Handcrafted Men & Women Products

1. I desire a clean, upscale looking label suite for a natural body luxury company called Leonard Ashby. It will include a sugar scrub label, shower gel, and beard oil to start. I handcraft skin-loving products using plant-based ingredients for men and women. My men's line includes beard oil, shower gel, sugar scrub, lotion, body spray, and soap. <br/>3. I use a black 8 oz jar for the scrub (see its specs attached). I attached my own mockup using Adobe Illustrator. It needs work and a professional redesign. I attached my only inspiration. Please use the colors brown, gray and silver in the example provided to include the gray texture.<br/>4 I use Tundra Tags for my custom product labels and they have requirements I provide with this link: https://www.tundratags.example/product-label-artwork<br/>5. I'd like each product to say, "NATURAL BODY LUXURY by LEONARD ASHBY".<br/>6. The logo is in the Adobe Illustrator file attached.<br/>

Industry/Entity Type

Skin Care Product

Font styles to use
Other font styles liked:
• Century Gothic or something similar

Colors

Designer to choose colors to be used in the design.

Requirements
Must have
• Clean and minimalist features, masculine upscale.
• Social media icons, FB, Chirper, IG.
• A label with the same colors, background texter design as example (brown, gray, silver).

```html
<!DOCTYPE html>
<html lang="en">
<head>
<meta charset="utf-8">
<title>Leonard Ashby – Emulsified Sugar Scrub Label</title>
<link rel="stylesheet" href="https://fonts.googleapis.com/css2?family=Questrial&family=Marcellus&display=swap">
<style>
  :root {
    --page: #ffffff;
    --slate-light: #55555b;
    --slate-mid: #3c3c41;
    --slate-dark: #232326;
    --copper: #d8995a;
    --copper-band: #e3a66a;
    --copper-band-light: #f0b97e;
    --silver: #c9c9ce;
    --silver-soft: #9d9da3;
    --ink: #1a1a1c;
    --white: #f4f4f4;
    --sans: "Questrial", "Century Gothic", sans-serif;
    --serif: "Marcellus", serif;
  }
  * { box-sizing: border-box; margin: 0; padding: 0; }
  html, body { width: 1200px; height: 905px; overflow: hidden; background: var(--page); }
  .canvas { position: relative; width: 1200px; height: 905px; }

  .label {
    position: absolute; left: 30px; top: 350px; width: 1140px; height: 204px;
    background:
      repeating-linear-gradient(90deg, rgba(255,255,255,0.025) 0 1px, transparent 1px 3px),
      linear-gradient(90deg, var(--slate-dark) 0%, var(--slate-light) 18%, var(--slate-mid) 38%, var(--slate-light) 55%, var(--slate-dark) 75%, var(--slate-light) 90%, var(--slate-dark) 100%);
    overflow: hidden;
  }

  /* left info column */
  .info-box {
    position: absolute; left: 19px; width: 324px;
    border: 1px solid var(--silver-soft); border-radius: 3px;
    padding: 2px 4px 2px 4px;
    font-family: var(--sans); font-size: 8.6px; line-height: 9.8px; color: var(--white);
    text-align: justify;
  }
  .info-box .tag {
    display: inline-block; background: var(--white); color: var(--ink);
    font-weight: 700; padding: 0 5px; border-radius: 0 6px 6px 0; margin-right: 4px;
  }
  .directions { top: 18px; height: 49px; }
  .caution { top: 71px; height: 25px; }
  .ingredients { top: 100px; height: 56px; }

  /* center panel */
  .panel {
    position: absolute; left: 430px; top: 9px; width: 279px; height: 143px;
    border: 2px solid var(--silver);
  }
  .panel::after {
    content: ""; position: absolute; inset: 3px; border: 1px solid var(--silver-soft);
  }
  .monogram {
    position: absolute; left: 0; right: 0; top: 20px;
    display: flex; align-items: center; justify-content: center; gap: 6px;
    font-family: var(--sans); font-size: 15px; color: var(--copper);
  }
  .monogram .dot { width: 16px; height: 16px; border: 2px solid var(--copper); border-radius: 50%; }
  .brand-name {
    position: absolute; left: 0; right: 0; top: 76px; text-align: center;
    font-family: var(--sans); font-size: 16px; color: var(--copper); letter-spacing: 0.3px;
  }
  .product-name {
    position: absolute; left: 0; right: 0; top: 100px; text-align: center;
    font-family: var(--serif); font-size: 17px; color: var(--white); letter-spacing: 0.6px;
  }
  .claim {
    position: absolute; left: 494px; top: 139px; width: 151px; height: 21px;
    background: linear-gradient(180deg, #2e2e31, #0d0d0e); border: 1px solid var(--silver);
    border-radius: 2px; text-align: center;
    font-family: var(--sans); font-size: 11px; line-height: 19px; color: var(--white); letter-spacing: 0.4px;
  }

  /* right column */
  .about {
    position: absolute; left: 811px; top: 20px; width: 282px;
    font-family: var(--sans); font-size: 8.6px; line-height: 9.8px; color: var(--white);
    text-align: justify;
  }
  .about p + p { margin-top: 8px; }
  .follow {
    position: absolute; left: 917px; top: 140px;
    display: flex; align-items: center; gap: 6px;
    font-family: var(--sans); font-size: 11px; color: var(--white);
  }
  .follow .network { display: flex; align-items: center; gap: 3px; font-size: 8.6px; color: var(--copper); }
  .follow .network i { display: block; width: 8px; height: 8px; background: var(--copper); border-radius: 2px; }

  /* bottom band */
  .band {
    position: absolute; left: 0; bottom: 0; width: 100%; height: 36px;
    background: linear-gradient(90deg, var(--copper-band), var(--copper-band-light) 50%, var(--copper-band));
  }
  .band-text { position: absolute; top: 12px; font-family: var(--serif); color: var(--ink); }
  .audience { left: 118px; font-size: 11.5px; }
  .scent { left: 489px; font-size: 12px; letter-spacing: 0.3px; }
  .volume { left: 671px; top: 14px; font-family: var(--sans); font-size: 8px; }
</style>
</head>
<body>
<main class="canvas">
  <section class="label" aria-label="Sugar scrub jar label">
    <div class="info-box directions"><span class="tag">Directions</span>Apply to clean skin during your bath or shower to gently exfoliate the skin and seal in moisture using circular motions over body avoiding the eyes. Concentrate on dry areas such as knees, heels, and elbows. Rinse well and towel dry skin.</div>
    <div class="info-box caution"><span class="tag">Exercise caution</span>during and after your bath routine since the oils can leave your bath area slippery.</div>
    <div class="info-box ingredients"><span class="tag">Ingredients</span>Sucrose, Prunus Amygdalus Dulcis (Sweet Almond) Oil, Simmondsia Chinensis (Jojoba) Seed Oil, Cocos Nucifera (Coconut) Oil, Olea Europaea (Olive) Oil Unsaponifiables, Cetearyl Alcohol, Essential &amp; Fragrance Oils, Stearic Acid, Beeswax, Phenoxyethanol (and) Caprylyl Glycol (and) Sorbic Acid (Presaphen Blend), Mica Colorant.</div>

    <div class="panel">
      <div class="monogram"><span class="dot"></span>Leonard Ashby</div>
      <div class="brand-name">LEONARD ASHBY</div>
      <div class="product-name">EMULSIFIED SUGAR SCRUB</div>
    </div>
    <div class="claim">HUMECTANT EXFOLIANT</div>

    <div class="about">
      <p>Leonard Ashby Naturals, Inc. is a handcrafted bath and body brand that is in part the result of the soap making tradition of the founder's mom, Ms. Ruth. Our body luxury brand is cruelty free and we are committed to the use of quality skin loving ingredients.</p>
      <p>Use Leonard Ashby emulsifying sugar scrub to gently exfoliate and remove dead skin cells to promote healthier, hydrated, softer skin.</p>
      <p>Handcrafted &amp; Distributed by Leonard Ashby Naturals, Inc., Millbrook, NY 10990. Visit us online for details about our other products at leonardashby.example and like or follow us on social media @lanaturalco.</p>
    </div>
    <div class="follow">Follow us on :
      <span class="network"><i></i>Facefolio</span>
      <span class="network"><i></i>Chirper</span>
      <span class="network"><i></i>Snapgram</span>
    </div>

    <div class="band" role="img" aria-label="Copper band with fine geometric line pattern">
      <span class="band-text audience">FOR THE GENTLEMAN</span>
      <span class="band-text scent">- OAKMOSS SANDALWOOD -</span>
      <span class="band-text volume">10 fl oz | 296 ml</span>
    </div>
  </section>
</main>
</body>
</html>
```